Health supplement brand needs a new logo for flagship product launch

I have attached a Word document to the brief which gives more detail.

There are 3 different products that we will sell. The label should be interchangeable across all 3 products, where only the colours change. This requires both a selection of a font typface to match our style and a new image embedded in the logo.

Target Market(s)

The target customer is women aged between 25 and 60. We would like to cross over between both audiences, without ruling one out

Font styles to use
Sans Serif

Requirements
Must have
• - It must be eye catching, i.e. people need to stop scrolling when they see it.
- It must have contemporary colours that are popular with women, i.e. pinks, apricots, dark greens, mustards, etc
- The image needs to be very feminine, just like the target audience
- The label must evoke some emotion, yet still be a little bit fun without being too serious.
- The label must use this image below as the main foundation. I have included the EPS file with this email.
Nice to have
• - We want to be somewhere in the middle, as in, the right price point accessible for most people, but still with a bit of class, fun and femininity
Should not have
• - We also don’t want it to look like “just another” nutritional brand selling Marrin Staples

```html
<!DOCTYPE html>
<html lang="en">
<head>
<meta charset="utf-8">
<title>Vitalune Collagen Calm Grace Label</title>
<link rel="stylesheet" href="https://fonts.googleapis.com/css2?family=Montserrat:wght@300;400;500;700&family=Great+Vibes&display=swap">
<style>
  :root {
    --white: #ffffff;
    --blush: #fbe7ef;
    --blush-deep: #f4c9da;
    --peach: #f3dccd;
    --rose: #c96f87;
    --brush: #f1a7b9;
    --brush-deep: #ea8fa6;
    --green: #3f9b74;
    --ink: #3a3a3a;
  }
  * { margin: 0; padding: 0; box-sizing: border-box; }
  html, body { width: 988px; height: 1200px; overflow: hidden; background: var(--white); }
  .label {
    position: relative;
    width: 988px;
    height: 1200px;
    overflow: hidden;
    background: var(--white);
    font-family: "Montserrat", Arial, sans-serif;
  }
  .brand-bar {
    position: absolute; top: 0; left: 0; width: 100%; height: 170px;
    display: flex; align-items: center; justify-content: center; gap: 14px;
  }
  .brand-name {
    font-weight: 300;
    font-size: 44px;
    letter-spacing: 9px;
    color: var(--ink);
  }
  .brand-dot {
    width: 16px; height: 16px; border-radius: 50%; background: var(--green);
  }
  .wash {
    position: absolute; top: 170px; left: 0; width: 100%; height: 1030px;
    background:
      radial-gradient(ellipse 320px 260px at 880px 260px, var(--blush-deep), transparent 70%),
      radial-gradient(ellipse 300px 360px at 270px 820px, #f0d6e4, transparent 70%),
      radial-gradient(ellipse 260px 200px at 150px 180px, var(--peach), transparent 70%),
      radial-gradient(ellipse 280px 320px at 860px 900px, var(--blush-deep), transparent 70%),
      linear-gradient(180deg, var(--blush) 0%, #fcedf3 100%);
  }
  .product-name {
    position: absolute; top: 245px; left: 0; width: 100%;
    text-align: center;
    font-weight: 500;
    font-size: 92px;
    letter-spacing: 1px;
    line-height: 1;
    color: var(--rose);
  }
  .brush-stroke {
    position: absolute; top: 372px; left: 105px; width: 790px; height: 205px;
    border-radius: 40px 90px 60px 30px / 60px 40px 80px 50px;
    background: linear-gradient(90deg, var(--brush) 0%, var(--brush-deep) 45%, var(--brush) 100%);
    opacity: 0.9;
  }
  .variant-name {
    position: absolute; top: 385px; left: 0; width: 100%;
    text-align: center;
    font-family: "Great Vibes", cursive;
    font-size: 150px;
    line-height: 1.2;
    color: var(--white);
  }
  .descriptor {
    position: absolute; top: 610px; left: 0; width: 100%;
    text-align: center;
    font-weight: 400;
    font-size: 28px;
    line-height: 1.2;
    color: var(--green);
  }
  .figure-art {
    position: absolute; top: 680px; left: 590px; width: 340px; height: 460px;
    border-radius: 45% 45% 20% 20%;
    background: linear-gradient(180deg, rgba(233,194,180,0.35), rgba(201,111,135,0.35));
  }
  .benefits {
    position: absolute; top: 1104px; left: 66px;
    font-weight: 700;
    font-size: 20.5px;
    line-height: 1.2;
    letter-spacing: 0.3px;
    color: var(--rose);
  }
  .baseline {
    position: absolute; top: 1135px; left: 0; width: 100%; height: 8px;
  }
</style>
</head>
<body>
  <main class="label">
    <header class="brand-bar">
      <span class="brand-name">VITALUNE</span>
      <span class="brand-dot"></span>
    </header>

    <div class="wash" role="img" aria-label="Soft pink and peach watercolour wash background"></div>

    <h1 class="product-name">COLLAGEN</h1>
    <div class="brush-stroke" role="img" aria-label="Pink watercolour brush stroke"></div>
    <p class="variant-name">Calm Grace</p>
    <p class="descriptor">Unflavoured 100% Bovine Collagen Powder</p>

    <div class="figure-art" role="img" aria-label="Single-line illustration of a seated woman in rose and peach tones"></div>

    <p class="benefits">HAIR | SKIN | NAILS | JOINTS | MUSCLES</p>
    <svg class="baseline" viewBox="0 0 988 8" preserveAspectRatio="none" aria-hidden="true">
      <line x1="0" y1="4" x2="988" y2="4" stroke="var(--rose)" stroke-width="2"/>
    </svg>
  </main>
</body>
</html>
```